New Fresh design for online Rabbit Game

Hi,

we are a french company working on a online rabbits game for kids, and not kids.

Our website is www.trovelu.fr, but you can look at the US version : www.hoplark.com

We buy our actual design 2 years ago, but we now think it's too boring and washed out...

We need yours talent to make a really more exacting, more colorful, fresh and dynamic design.

In our game, players have to breed and train rabbits and to make them run races. Players run again friends or players.

Players are kids, between 8 and 15 years. But best players are often parents of these kids !

Our ambiance is clearly funny. We really like if color theme or background look like a nice blue sky, and / or beach. Something that make people happy to come, and say "You are here on holly days to have fun !"

I think the best is if we have 2 layouts, one for the Home page, and one for all other page.

For home page, we are really open to any proposition, we just need to keep our features :
- registration (with rabbit preview)
- connection
- game preview (images slide with small text)
- live race preview (as we have actually)

For other pages layout, we need a layout with a standard container (maybe 850 px width?), and our 2 navigation's bar.

We only need psd, no html integration.

Thanks for your help, please ask me for any questions.
Updates

Hi, 

I have just added some information, concerning layout.

Also we have just committed the budget.

Target Market(s)

Mostly kids between 8 and 15 years.

Industry/Entity Type

It Company

Requirements
Must have
• We already have some characters, like Mr Pebblo at the home page and our rabbits. We want to keep all of them, so new design have to match with there style (carton).

If you create an account, you will see we have a big nav bar with 6 tabs, and a little top bar. We absolutely need them to keep a easy navigation in website.

We also need some proposition of element style, like h1, h2, h3, hr, inputs, buttons, notification bubble, etc... So we can work to improve all our pages.
Nice to have
• I think the actual website is a little to wide (about 1000px width). Maybe something like 900px - 850px is more elegant ?
In this case, we can arrange pages to deal with it.

It can be cool if major colors are stil blue and green, to match a little with actual colors. But it's no very important.
Should not have
• We don't want too big header picture (for the all pages layout). I mean, players have to focus on the content.

We don't want photo realistic style, our style is cartoon.

We don't want flash. But Js animations are ok.

```html
<!DOCTYPE html>
<html lang="fr">
<head>
<meta charset="utf-8">
<title>trovelu.fr – Accueil</title>
<link rel="stylesheet" href="https://fonts.googleapis.com/css2?family=Arimo:wght@400&family=Delius&family=Caveat:wght@400;600&family=Kalam:wght@400&display=swap">
<style>
  :root {
    --sky-top: #2a8fd6;
    --sky-bottom: #7fd0f2;
    --ground: #f1f1f1;
    --footer: #d6d6d6;
    --white: #ffffff;
    --brand-dot: #23659a;
    --nav-active: #3f8fc8;
    --ink: #1c3550;
    --red: #e3231d;
    --yellow: #f5e326;
    --reg-blue: #35b4ea;
    --reg-ring: #cde8f2;
    --login-grey: #e4e6e6;
    --login-ring: #e9e16a;
    --login-title: #b3981e;
    --field-grey: #858585;
    --panel-line: #c9a98c;
    --menu-orange: #c96a1e;
    --body-text: #333333;
    --footer-text: #666666;
  }
  * { box-sizing: border-box; margin: 0; padding: 0; }
  html, body { width: 1200px; height: 1136px; overflow: hidden; }
  body {
    position: relative;
    font-family: "Arimo", Arial, sans-serif;
    background: var(--ground);
    color: var(--body-text);
  }
  .abs { position: absolute; }

  .sky {
    position: absolute; left: 0; top: 0; width: 1200px; height: 583px;
    background: linear-gradient(180deg, var(--sky-top) 0%, #4fb2e8 40%, var(--sky-bottom) 75%, #cfeaf6 100%);
  }
  .cloud { position: absolute; background: rgba(255,255,255,0.75); border-radius: 50%; filter: blur(6px); }

  .brand { position: absolute; left: 72px; top: 44px; display: flex; align-items: center; gap: 12px; }
  .brand-dot { width: 34px; height: 34px; border-radius: 50%; background: var(--brand-dot); flex: none; }
  .brand-name {
    font-family: "Delius", cursive; font-size: 38px; line-height: 48px; color: var(--white); white-space: nowrap;
  }

  .main-nav { position: absolute; top: 49px; left: 635px; height: 36px; }
  .main-nav a {
    position: absolute; top: 0; height: 36px; line-height: 36px;
    font-family: "Delius", cursive; font-size: 20px; color: var(--white); text-decoration: none;
    text-shadow: 0 1px 2px rgba(0,0,0,0.25);
  }
  .main-nav a.active { background: var(--nav-active); border-radius: 5px; padding: 0 16px; box-shadow: 0 1px 3px rgba(0,0,0,0.3); }

  .tagline { font-family: "Caveat", cursive; white-space: nowrap; }
  .tagline-1 { left: 486px; top: 162px; font-size: 48px; color: var(--ink); }
  .tagline-2 { left: 733px; top: 224px; font-size: 48px; color: var(--red); }

  .hero-character {
    left: 107px; top: 171px; width: 334px; height: 433px;
    border-radius: 48% 48% 40% 40%;
    background: radial-gradient(ellipse at 50% 45%, #e6d93a 0%, #8fb83a 45%, #6b6a2c 80%, rgba(107,106,44,0) 100%);
  }

  .signup {
    left: 398px; top: 251px; width: 386px; height: 386px; border-radius: 50%;
    background: var(--reg-ring);
  }
  .signup-inner {
    position: absolute; left: 8px; top: 8px; width: 370px; height: 370px; border-radius: 50%;
    background: var(--reg-blue);
  }
  .signup-title { left: 596px; top: 282px; transform: translateX(-50%); font-family: "Delius", cursive; font-size: 23px; color: var(--white); white-space: nowrap; }
  .signup-sub { left: 531px; top: 309px; font-family: "Delius", cursive; font-size: 15px; color: var(--yellow); white-space: nowrap; }
  .step { font-size: 12.5px; white-space: nowrap; }
  .step-1 { left: 453px; top: 342px; color: var(--red); }
  .rabbit-name { left: 467px; top: 362px; color: var(--white); font-size: 14.5px; }
  .rabbit-preview { left: 437px; top: 384px; width: 60px; height: 55px; border-radius: 40%; background: radial-gradient(ellipse, #f2e6c9 0%, rgba(242,230,201,0) 75%); }
  .option { position: absolute; left: 510px; width: 88px; height: 16px; display: flex; align-items: center; justify-content: space-between; font-size: 12px; color: var(--white); }
  .option svg { width: 18px; height: 12px; flex: none; }
  .rule { height: 1px; background: rgba(255,255,255,0.55); }
  .step-2 { left: 611px; top: 470px; transform: translateX(-50%); color: #0d2b45; }
  .pseudo-field { left: 544px; top: 495px; width: 168px; height: 31px; border-radius: 16px; background: var(--white); }
  .go-arrow { left: 718px; top: 498px; width: 30px; height: 24px; }
  .step-3 { left: 485px; top: 544px; color: #0d2b45; }

  .btn-play {
    position: absolute; height: 31px; border: 3px solid #12384f; border-radius: 5px;
    background: var(--reg-blue); font-family: "Kalam", cursive; font-size: 16px; color: var(--ink);
    display: flex; align-items: center; justify-content: center; box-shadow: inset 0 0 0 2px rgba(255,255,255,0.4);
  }
  .btn-play.signup-btn { left: 509px; top: 570px; width: 88px; }
  .btn-play.login-btn { left: 855px; top: 567px; width: 90px; background: var(--login-grey); }

  .login {
    left: 753px; top: 355px; width: 288px; height: 288px; border-radius: 50%;
    background: var(--login-grey); border: 7px solid var(--login-ring);
  }
  .login-title { left: 897px; top: 398px; transform: translateX(-50%); font-family: "Delius", cursive; font-size: 21px; color: var(--login-title); }
  .login-label { left: 776px; font-size: 12px; color: #333; white-space: nowrap; }
  .login-field { left: 856px; width: 166px; height: 27px; border-radius: 14px; background: var(--field-grey); }
  .forgot { left: 914px; top: 530px; transform: translateX(-50%); font-size: 10.5px; color: #333; white-space: nowrap; }

  .panel { position: absolute; top: 673px; height: 314px; border: 1px solid var(--panel-line); background: #f4f4f4; overflow: hidden; }
  .panel-preview { left: 107px; width: 521px; }
  .panel-races { left: 679px; width: 407px; }
  .panel-title { position: absolute; font-family: "Delius", cursive; font-size: 14.5px; color: #444; white-space: nowrap; }
  .panel-rule { position: absolute; height: 1px; background: #b5b5b5; }
  .panel-icon { position: absolute; left: 9px; top: 14px; width: 30px; height: 28px; border-radius: 6px; background: linear-gradient(135deg, #f3d98a, #d6b15a); }
  .game-menu { position: absolute; left: 48px; top: 79px; list-style: none; }
  .game-menu li { height: 26.5px; font-size: 12.5px; color: var(--menu-orange); }
  .menu-divider { position: absolute; left: 135px; top: 56px; width: 1px; height: 238px; background: #d3a680; }
  .preview-art { position: absolute; left: 167px; top: 0; width: 318px; height: 314px; border-radius: 46% 46% 8px 8px; background: radial-gradient(ellipse at 50% 55%, #8a7bb8 0%, #7a5f3c 55%, rgba(122,95,60,0.15) 100%); }
  .race-art { position: absolute; left: 1px; top: 46px; width: 228px; height: 268px; border-radius: 45% 45% 10px 10px; background: radial-gradient(ellipse at 50% 45%, #a89a72 0%, #5f573c 60%, rgba(95,87,60,0.2) 100%); }
  .race-text { position: absolute; left: 233px; top: 78px; width: 165px; font-size: 10.5px; line-height: 15.2px; text-align: justify; color: #333; }

  .footer { position: absolute; left: 0; top: 1022px; width: 1200px; height: 114px; background: var(--footer); }
  .partners-label { left: 117px; top: 1051px; font-size: 12.5px; color: #555; }
  .badge { position: absolute; top: 1053px; width: 84px; height: 29px; border-radius: 2px; }
  .partners-line { left: 115px; top: 1109px; font-size: 9px; color: var(--footer-text); white-space: nowrap; }
  .contact { left: 701px; top: 1034px; list-style: none; font-size: 9.5px; color: var(--footer-text); }
  .contact li { height: 19px; }
  .legal { left: 903px; top: 1043px; font-size: 9.5px; color: var(--footer-text); white-space: nowrap; }
  .social { position: absolute; top: 1082px; width: 34px; height: 34px; border-radius: 50%; box-shadow: 0 2px 3px rgba(0,0,0,0.25); }
</style>
</head>
<body>

<div class="sky">
  <div class="cloud" style="left:620px;top:150px;width:260px;height:140px;"></div>
  <div class="cloud" style="left:820px;top:230px;width:380px;height:200px;"></div>
  <div class="cloud" style="left:930px;top:370px;width:280px;height:190px;"></div>
  <div class="cloud" style="left:0;top:430px;width:230px;height:150px;opacity:0.6;"></div>
  <div class="cloud" style="left:420px;top:420px;width:160px;height:120px;opacity:0.6;"></div>
</div>

<header>
  <div class="brand">
    <span class="brand-dot"></span>
    <span class="brand-name">trovelu.fr</span>
  </div>
  <nav class="main-nav">
    <a class="active" href="#" style="left:0;">Accueil</a>
    <a href="#" style="left:123px;">News</a>
    <a href="#" style="left:216px;">Forum</a>
    <a href="#" style="left:316px;">Records</a>
    <a href="#" style="left:433px;">Aide</a>
  </nav>
</header>

<p class="abs tagline tagline-1">Le plus cool des jeux d'élevages</p>
<p class="abs tagline tagline-2">et de course de lapins !</p>

<div class="abs hero-character" role="img" aria-label="Illustration de la mascotte du jeu"></div>

<section class="abs signup" aria-label="Nouveau joueur"><div class="signup-inner"></div></section>
<h2 class="abs signup-title">Nouveau joueur</h2>
<p class="abs signup-sub">Inscription en 3 secondes !</p>
<p class="abs step step-1">1 - Choisissez votre lapin</p>
<p class="abs step rabbit-name">Jade</p>
<div class="abs rabbit-preview" role="img" aria-label="Aperçu du lapin choisi"></div>

<div class="option" style="top:384px;">
  <svg viewBox="0 0 18 12"><path d="M1 6 L8 1 L8 4 L17 4 L17 8 L8 8 L8 11 Z" fill="#f3c79a" stroke="#7a4a22" stroke-width="1"/></svg>
  <span>Originale</span>
  <svg viewBox="0 0 18 12"><path d="M17 6 L10 1 L10 4 L1 4 L1 8 L10 8 L10 11 Z" fill="#f3c79a" stroke="#7a4a22" stroke-width="1"/></svg>
</div>
<div class="option" style="top:406px;">
  <svg viewBox="0 0 18 12"><path d="M1 6 L8 1 L8 4 L17 4 L17 8 L8 8 L8 11 Z" fill="#f3c79a" stroke="#7a4a22" stroke-width="1"/></svg>
  <span>Gris</span>
  <svg viewBox="0 0 18 12"><path d="M17 6 L10 1 L10 4 L1 4 L1 8 L10 8 L10 11 Z" fill="#f3c79a" stroke="#7a4a22" stroke-width="1"/></svg>
</div>
<div class="option" style="top:430px;">
  <svg viewBox="0 0 18 12"><path d="M1 6 L8 1 L8 4 L17 4 L17 8 L8 8 L8 11 Z" fill="#f3c79a" stroke="#7a4a22" stroke-width="1"/></svg>
  <span>Mâle</span>
  <svg viewBox="0 0 18 12"><path d="M17 6 L10 1 L10 4 L1 4 L1 8 L10 8 L10 11 Z" fill="#f3c79a" stroke="#7a4a22" stroke-width="1"/></svg>
</div>

<div class="abs rule" style="left:454px;top:460px;width:293px;"></div>
<p class="abs step step-2">2 - Choisissez un pseudo</p>
<div class="abs pseudo-field"></div>
<svg class="abs go-arrow" viewBox="0 0 30 24"><path d="M2 8 L17 8 L17 2 L28 12 L17 22 L17 16 L2 16 Z" fill="#f3c79a" stroke="#7a4a22" stroke-width="1.5"/></svg>
<div class="abs rule" style="left:454px;top:537px;width:293px;"></div>
<p class="abs step step-3">3 - C'est parti</p>
<div class="btn-play signup-btn">Jouer!</div>

<section class="abs login" aria-label="Connexion"></section>
<h2 class="abs login-title">Connexion</h2>
<p class="abs login-label" style="top:464px;">Pseudo :</p>
<div class="abs login-field" style="top:456px;"></div>
<p class="abs login-label" style="top:499px;">Mot de passe :</p>
<div class="abs login-field" style="top:491px;"></div>
<p class="abs forgot">Mot de passe oublié ?</p>
<div class="btn-play login-btn">Jouer!</div>

<section class="panel panel-preview">
  <div class="panel-icon" role="img" aria-label="Icône d'aperçu"></div>
  <h3 class="panel-title" style="left:46px;top:23px;">Aperçu du jeu</h3>
  <div class="panel-rule" style="left:43px;top:42px;width:461px;"></div>
  <ul class="game-menu">
    <li>Votre parc</li><li>Votre jardin</li><li>Les métiers</li><li>L'univers</li>
    <li>Votre parc</li><li>Votre jardin</li><li>Les métiers</li><li>L'univers</li>
  </ul>
  <div class="menu-divider"></div>
  <div class="preview-art" role="img" aria-label="Illustration d'un savant préparant des légumes"></div>
</section>

<section class="panel panel-races">
  <h3 class="panel-title" style="left:16px;top:22px;">Participez aux courses avec d'autres joueurs</h3>
  <div class="panel-rule" style="left:7px;top:42px;width:392px;"></div>
  <div class="race-art" role="img" aria-label="Illustration d'un personnage jardinier avec une pelle"></div>
  <p class="race-text">Lorem ipsum dolor sit amet, consectetur adipisicing elit, sed do eiusmod tempor incididunt ut labore et dolore magna aliqua. Ut enim ad minim veniam, quis nostrud exercitation ullamco laboris nisi ut aliquip ex ea commodo consequat. Duis aute irure dolor in reprehenderit in voluptate velit esse cillum dolore eu fugiat nulla pariatur. Excepteur sint occaecat cupidatat non proident, sunt in culpa qui officia deserunt mollit anim id est</p>
</section>

<footer class="footer"></footer>
<p class="abs partners-label">Partenaires :</p>
<div class="badge" style="left:200px;background:#8fc8e8;"></div>
<div class="badge" style="left:301px;background:#2a7fd0;"></div>
<div class="badge" style="left:400px;background:#b02a9a;"></div>
<div class="badge" style="left:497px;background:#3a1e1e;border-radius:6px;"></div>
<p class="abs partners-line">Partenaires : Jeux - Jeux de course - Jeux d'élevage - Jeu gratuit du net - Jeu en ligne - Jeux en ligne - jeux gratuits - voir tous</p>
<ul class="abs contact">
  <li>Email id:</li>
  <li>Phone No.:</li>
  <li>Fax No.:</li>
  <li>Address : Line 1</li>
  <li style="padding-left:46px;">Line2</li>
</ul>
<p class="abs legal">Règlement - CGU - Contact - Trovelu.fr 3.0</p>
<div class="social" style="left:946px;background:#2b9de0;"></div>
<div class="social" style="left:988px;background:#f27a1c;"></div>
<div class="social" style="left:1030px;background:#8a8a8a;"></div>

</body>
</html>
```